Machine shop needs a brochure designed

Would like a tri-fold professional looking brochure that tells about our business and our capabilities. We are a family-owned business with over 50 years of experience in precision manufacturing. We specialize in close-tolerance tooling and serve a diverse array of industries. Our colors are red, black, white, and gray. The final design should make a great impression and spotlight our capabilities and quality.

Target Market(s)

Manufacturing industries needing tooling

Industry/Entity Type

Machining, grinding, manufacturing

Font styles to use
Serif

Colors
EB3D1F
EC4F4E
F09395
F8D3D4
FCEDEE

Requirements
Must have
• Logo, colors are red, black, white, gray
Nice to have
• Images of CNC process or machining/grinding metal parts.

```html
<!DOCTYPE html>
<html lang="en">
<head>
<meta charset="utf-8">
<title>Norvale Industries – Tri-fold Brochure</title>
<link href="https://fonts.googleapis.com/css2?family=Montserrat:wght@400;600;700;800&family=Open+Sans:wght@400;600;700&display=swap" rel="stylesheet">
<style>
:root{
  --red:#d9232a;
  --red-dark:#a9161c;
  --ink:#1c1c1e;
  --charcoal:#262629;
  --charcoal-2:#323236;
  --gray:#6d6e71;
  --light:#f2f2f2;
  --white:#ffffff;
  --bg:#e4e4e4;
}
*{box-sizing:border-box;margin:0;padding:0}
html,body{width:1200px;height:2400px;overflow:hidden}
body{background:var(--bg);font-family:"Open Sans",Arial,sans-serif;color:var(--ink);position:relative}
.spread{position:absolute;left:50px;width:1100px;height:850px;display:flex;box-shadow:0 10px 30px rgba(0,0,0,.18)}
.spread--outside{top:250px}
.spread--inside{top:1300px}
.panel{position:relative;width:366.66px;height:850px;overflow:hidden}
.panel--white{background:var(--white)}
.panel--dark{background:linear-gradient(160deg,var(--charcoal-2),var(--ink));color:var(--white)}
.shape{position:absolute;left:0;width:100%;display:block}
.photo{position:absolute;left:0;width:100%}
.brand{display:flex;align-items:center;gap:12px}
.brand__mark{width:34px;height:34px;background:var(--red);flex:none}
.brand__name{font-family:"Montserrat",Arial,sans-serif;font-weight:600;font-size:26px;color:var(--ink)}
.brand--light .brand__name{color:var(--white)}
.heading{font-family:"Montserrat",Arial,sans-serif;font-weight:800;font-size:17px;text-transform:uppercase;color:var(--ink);line-height:1.2}
.rule{width:46px;height:3px;background:var(--red);margin:8px 0 14px}
.copy{font-size:11.5px;line-height:1.65;color:#3a3a3c;margin-bottom:10px}
.web{font-family:"Montserrat",Arial,sans-serif;font-weight:700;font-size:14px}
.web svg{vertical-align:-3px;margin-right:8px}
.badge{position:absolute;width:58px;height:58px;border-radius:50%;background:#8c8d90;border:3px solid #d5d5d5}

/* outside: about */
.about{position:absolute;top:92px;left:34px;right:34px}
.signoff{display:flex;justify-content:space-between;font-size:11px;margin-top:14px;color:#3a3a3c}
.signoff strong{display:block;font-weight:700;color:var(--ink)}
.about-foot{position:absolute;bottom:0;left:0;right:0;height:128px}
.about-foot__msg{position:absolute;left:34px;right:34px;top:28px;color:var(--white);font-size:11.5px;line-height:1.5;text-align:center}
.about-foot__bar{position:absolute;bottom:0;left:0;right:0;height:42px;background:var(--ink);color:var(--white);display:flex;align-items:center;padding-left:30px}

/* outside: contact */
.contact{position:absolute;top:110px;left:30px;right:30px;text-align:center}
.contact .brand{justify-content:center;margin-bottom:36px}
.contact__lead{font-family:"Montserrat",Arial,sans-serif;font-size:16px;line-height:1.45;margin-bottom:26px}
.contact__addr{font-size:12px;line-height:1.7;color:#d7d7d9;margin-bottom:18px}
.contact__web{background:var(--red);color:var(--white);padding:9px 0;margin:0 -30px 12px;font-family:"Montserrat",Arial,sans-serif;font-weight:700;font-size:15px}
.contact__mail{font-size:12px;color:#d7d7d9}

/* outside: cover */
.cover__top{position:absolute;top:0;left:0;right:0;height:230px;background:linear-gradient(180deg,#fff,#ececec);clip-path:polygon(0 0,100% 0,100% 72%,50% 100%,0 72%)}
.cover .brand{position:absolute;top:70px;left:0;right:0;justify-content:center}
.cover__band{position:absolute;left:0;right:0;top:600px;height:200px;background:var(--red);clip-path:polygon(0 22%,100% 0,100% 100%,0 100%)}
.cover__tagline{position:absolute;left:0;right:0;top:672px;text-align:center;font-family:"Montserrat",Arial,sans-serif;font-weight:800;font-size:23px;line-height:1.2;color:var(--white);text-transform:uppercase}
.cover__bar{position:absolute;bottom:0;left:0;right:0;height:56px;background:var(--ink);color:var(--white);display:flex;align-items:center;justify-content:center}

/* inside: welcome */
.welcome{position:absolute;top:70px;left:34px;right:34px}
.welcome .heading{padding-right:70px}
.welcome .web{color:var(--red);margin-top:14px}

/* inside: capabilities */
.caps{position:absolute;top:40px;left:32px;right:32px}
.caps__label{display:inline-block;background:var(--red);color:var(--white);font-family:"Montserrat",Arial,sans-serif;font-weight:800;font-size:15px;padding:7px 22px;margin:0 0 18px 40px}
.caps__intro{font-size:12.5px;line-height:1.5;text-align:center;margin-bottom:10px}
.caps__sub{font-size:12px;text-align:center;margin-bottom:18px;color:#d7d7d9}
.caps__list{list-style:none}
.caps__list li{display:flex;gap:10px;font-size:12.5px;line-height:1.4;margin-bottom:8px}
.caps__list svg{flex:none;margin-top:1px}
.caps__foot{position:absolute;bottom:34px;left:0;right:0;text-align:center}
.caps__foot p{font-size:12.5px;line-height:1.45;margin:0 40px 12px}
.caps__foot .contact__web{margin:0}

/* inside: quality */
.quality{position:absolute;top:420px;left:34px;right:34px}
.quality .heading{font-size:15px;padding-right:70px}
.quality .brand{position:absolute;left:0;bottom:-250px}
</style>
</head>
<body>

<!-- OUTSIDE SPREAD -->
<section class="spread spread--outside">
  <!-- back panel: about -->
  <article class="panel panel--white">
    <svg class="shape" style="top:0" width="367" height="70" viewBox="0 0 367 70" preserveAspectRatio="none" aria-hidden="true">
      <path d="M0 0H367V22C260 62 120 6 0 44Z" fill="var(--red)"/>
      <path d="M0 44C120 6 260 62 367 22V30C260 70 120 16 0 52Z" fill="var(--ink)"/>
    </svg>
    <div class="about">
      <h2 class="heading">About Us</h2>
      <div class="rule"></div>
      <p class="copy">Norvale Industries, Inc. is a privately owned precision machine shop with over 50 years of experience in precision manufacturing. We began as a small family shop and have grown into a trusted partner for tooling across many industries.</p>
      <p class="copy">Our skilled machinists use modern CNC equipment and proven methods to hold close tolerances on every part we produce, from single prototypes to full production runs.</p>
      <p class="copy">We look forward to working with you and thank you for the opportunity to earn your business.</p>
      <p class="copy">Best regards,</p>
      <div class="signoff">
        <span><strong>Daniel R. Hollis</strong>Owner / President</span>
        <span><strong>Mark Hollis</strong>CEO</span>
      </div>
    </div>
    <div class="about-foot">
      <svg class="shape" style="top:0" width="367" height="128" viewBox="0 0 367 128" preserveAspectRatio="none" aria-hidden="true">
        <path d="M0 20C120 0 250 30 367 6V128H0Z" fill="var(--red)"/>
      </svg>
      <p class="about-foot__msg">Contact us today and let us help you make your product a success!</p>
      <div class="about-foot__bar web">
        <svg width="16" height="16" viewBox="0 0 16 16" aria-hidden="true"><circle cx="8" cy="8" r="7" fill="none" stroke="#fff" stroke-width="1.5"/><path d="M1 8h14M8 1c3 3 3 11 0 14M8 1c-3 3-3 11 0 14" fill="none" stroke="#fff" stroke-width="1.2"/></svg>www.norvaleindustries.net
      </div>
    </div>
  </article>

  <!-- middle panel: contact -->
  <article class="panel panel--dark">
    <div class="contact">
      <div class="brand brand--light"><span class="brand__mark"></span><span class="brand__name">Norvale Industries</span></div>
      <p class="contact__lead">Contact us today and let us help you make your product a success!</p>
      <p class="contact__addr">4820 Harlan Creek Road<br>Millbrook, TN 37000</p>
      <p class="contact__web">www.norvaleindustries.net</p>
      <p class="contact__addr">615-555-0142<br>info@norvaleindustries.net</p>
    </div>
    <div class="photo" style="bottom:0;height:300px;background:radial-gradient(circle at 55% 45%,#f0b45a 0,#8a5a2a 12%,#2c2c30 45%,#141416 100%)" role="img" aria-label="Photo of a CNC cutting head throwing sparks on a dark shop floor"></div>
  </article>

  <!-- front cover -->
  <article class="panel panel--dark cover">
    <div class="photo" style="top:150px;height:520px;background:radial-gradient(circle at 50% 40%,#f5b04a 0,#b36a24 14%,#4a4a4f 45%,#1e1e21 100%)" role="img" aria-label="Photo of a laser cutter spraying orange sparks over a metal part"></div>
    <div class="cover__top"></div>
    <div class="brand"><span class="brand__mark"></span><span class="brand__name">Norvale Industries</span></div>
    <div class="cover__band"></div>
    <p class="cover__tagline">Precise, High-Quality<br>Components</p>
    <div class="cover__bar web">
      <svg width="16" height="16" viewBox="0 0 16 16" aria-hidden="true"><circle cx="8" cy="8" r="7" fill="none" stroke="#fff" stroke-width="1.5"/><path d="M1 8h14M8 1c3 3 3 11 0 14M8 1c-3 3-3 11 0 14" fill="none" stroke="#fff" stroke-width="1.2"/></svg>www.norvaleindustries.net
    </div>
  </article>
</section>

<!-- INSIDE SPREAD -->
<section class="spread spread--inside">
  <!-- welcome -->
  <article class="panel panel--white">
    <svg class="shape" style="top:0" width="367" height="40" viewBox="0 0 367 40" preserveAspectRatio="none" aria-hidden="true">
      <path d="M0 0H367V10C250 34 120 4 0 24Z" fill="var(--red)"/>
    </svg>
    <span class="badge" style="top:70px;right:30px"></span>
    <div class="welcome">
      <h2 class="heading">Welcome<br>to Norvale Industries, Inc.</h2>
      <div class="rule"></div>
      <p class="copy">When your project or process requires precise, high-quality parts or components, look no further than Norvale.</p>
      <p class="copy">We welcome the opportunity to quote your project, and with 50 years combined experience in precision manufacturing, you can rest assured that you will be pleased with our work every time.</p>
      <p class="copy">Norvale Industries, Inc. is committed to quality and consistency. We are constantly striving to improve and meet the needs of our customers, providing on-time delivery and fair pricing on every order.</p>
      <p class="web">
        <svg width="16" height="16" viewBox="0 0 16 16" aria-hidden="true"><circle cx="8" cy="8" r="7" fill="none" stroke="var(--red)" stroke-width="1.5"/><path d="M1 8h14M8 1c3 3 3 11 0 14M8 1c-3 3-3 11 0 14" fill="none" stroke="var(--red)" stroke-width="1.2"/></svg>www.norvaleindustries.net
      </p>
    </div>
    <div class="photo" style="bottom:0;height:290px;background:linear-gradient(135deg,#2a3440,#4d5866 45%,#c98a2e 80%,#3a3a3e)" role="img" aria-label="Photo of an engineer with a tablet overseeing robotic machining equipment"></div>
    <svg class="shape" style="bottom:262px" width="367" height="40" viewBox="0 0 367 40" preserveAspectRatio="none" aria-hidden="true">
      <path d="M0 40V14C120 40 250 0 367 18V40Z" fill="var(--red)"/>
    </svg>
  </article>

  <!-- capabilities -->
  <article class="panel panel--dark">
    <div class="caps">
      <span class="caps__label">CAPABILITIES</span>
      <p class="caps__intro">We at Norvale offer a wide variety of services to meet your machining and tooling needs.</p>
      <p class="caps__sub">Our capabilities include:</p>
      <ul class="caps__list">
        <li><svg width="15" height="15" viewBox="0 0 15 15" aria-hidden="true"><rect width="15" height="15" rx="2" fill="var(--red)"/><path d="M3.5 7.5l2.6 2.6 5.4-5.4" fill="none" stroke="#fff" stroke-width="2"/></svg>Soft cutting</li>
        <li><svg width="15" height="15" viewBox="0 0 15 15" aria-hidden="true"><rect width="15" height="15" rx="2" fill="var(--red)"/><path d="M3.5 7.5l2.6 2.6 5.4-5.4" fill="none" stroke="#fff" stroke-width="2"/></svg>Hard cutting</li>
        <li><svg width="15" height="15" viewBox="0 0 15 15" aria-hidden="true"><rect width="15" height="15" rx="2" fill="var(--red)"/><path d="M3.5 7.5l2.6 2.6 5.4-5.4" fill="none" stroke="#fff" stroke-width="2"/></svg>CNC Machining</li>
        <li><svg width="15" height="15" viewBox="0 0 15 15" aria-hidden="true"><rect width="15" height="15" rx="2" fill="var(--red)"/><path d="M3.5 7.5l2.6 2.6 5.4-5.4" fill="none" stroke="#fff" stroke-width="2"/></svg>Grinding: OD / ID and Surface/Rotary (Carbide, Steel, etc.)</li>
        <li><svg width="15" height="15" viewBox="0 0 15 15" aria-hidden="true"><rect width="15" height="15" rx="2" fill="var(--red)"/><path d="M3.5 7.5l2.6 2.6 5.4-5.4" fill="none" stroke="#fff" stroke-width="2"/></svg>0-2 Micro-finishing</li>
        <li><svg width="15" height="15" viewBox="0 0 15 15" aria-hidden="true"><rect width="15" height="15" rx="2" fill="var(--red)"/><path d="M3.5 7.5l2.6 2.6 5.4-5.4" fill="none" stroke="#fff" stroke-width="2"/></svg>Light fabrication</li>
        <li><svg width="15" height="15" viewBox="0 0 15 15" aria-hidden="true"><rect width="15" height="15" rx="2" fill="var(--red)"/><path d="M3.5 7.5l2.6 2.6 5.4-5.4" fill="none" stroke="#fff" stroke-width="2"/></svg>Conveyor assemblies: slats, rollers, etc.</li>
        <li><svg width="15" height="15" viewBox="0 0 15 15" aria-hidden="true"><rect width="15" height="15" rx="2" fill="var(--red)"/><path d="M3.5 7.5l2.6 2.6 5.4-5.4" fill="none" stroke="#fff" stroke-width="2"/></svg>Can tooling: Trimmer Knives, Knockouts, Punch Rolls, Pocket Mandrels, Cut Edges, Blank and Draw Dies, etc.</li>
        <li><svg width="15" height="15" viewBox="0 0 15 15" aria-hidden="true"><rect width="15" height="15" rx="2" fill="var(--red)"/><path d="M3.5 7.5l2.6 2.6 5.4-5.4" fill="none" stroke="#fff" stroke-width="2"/></svg>Wide range of Aerospace and Automotive tooling</li>
        <li><svg width="15" height="15" viewBox="0 0 15 15" aria-hidden="true"><rect width="15" height="15" rx="2" fill="var(--red)"/><path d="M3.5 7.5l2.6 2.6 5.4-5.4" fill="none" stroke="#fff" stroke-width="2"/></svg>NAICS 332813, 332721 &amp; 333512</li>
        <li><svg width="15" height="15" viewBox="0 0 15 15" aria-hidden="true"><rect width="15" height="15" rx="2" fill="var(--red)"/><path d="M3.5 7.5l2.6 2.6 5.4-5.4" fill="none" stroke="#fff" stroke-width="2"/></svg>DUNS 07-482-1165</li>
        <li><svg width="15" height="15" viewBox="0 0 15 15" aria-hidden="true"><rect width="15" height="15" rx="2" fill="var(--red)"/><path d="M3.5 7.5l2.6 2.6 5.4-5.4" fill="none" stroke="#fff" stroke-width="2"/></svg>Reverse engineering services</li>
      </ul>
    </div>
    <div class="caps__foot">
      <p>Contact us today and let us help you make your product a success!</p>
      <p class="contact__web">www.norvaleindustries.net</p>
    </div>
  </article>

  <!-- quality -->
  <article class="panel panel--white">
    <div class="photo" style="top:0;height:330px;background:radial-gradient(circle at 40% 40%,#9a9ca1 0,#55575c 35%,#1f1f22 100%)" role="img" aria-label="Close-up photo of a CNC machine spindle cutting a steel part"></div>
    <svg class="shape" style="top:300px" width="367" height="70" viewBox="0 0 367 70" preserveAspectRatio="none" aria-hidden="true">
      <path d="M0 30C120 0 250 40 367 10V34C250 64 120 24 0 54Z" fill="var(--red)"/>
      <path d="M0 54C120 24 250 64 367 34V70H0Z" fill="var(--white)"/>
    </svg>
    <span class="badge" style="top:392px;right:30px"></span>
    <div class="quality">
      <h2 class="heading">Norvale Industries Quality Assurance</h2>
      <div class="rule"></div>
      <p class="copy">We are a family-owned business with over 50 years of experience in precision manufacturing. We specialize in close-tolerance tooling and serve a diverse array of industries.</p>
      <p class="copy">Norvale Industries, Inc. is committed to quality and consistency. Every part is inspected to strict standards before it leaves our shop.</p>
      <p class="copy">It is not only our goal, but we understand it is our responsibility to provide our clients with the highest quality products.</p>
    </div>
    <div class="brand" style="position:absolute;left:34px;bottom:40px"><span class="brand__mark"></span><span class="brand__name">Norvale Industries</span></div>
  </article>
</section>

</body>
</html>
```